Medical Software Informational Flyer and Website Design

Our company, Copper Vale Systems, is launching a new product, the Copper Vale Clinic Flow Platform. It is a software suite that will increase the productivity and volume of a LASIK practice.

We want this flyer to be a companion to our big reveal presentation at OPX and NVCSE; it's primary purpose is to inform potential clients on the many ways this software will help their practice. It is also obviously a promotional material. Because it is a companion to our presentation, we feel that it is acceptable for the flyer to contain much more text than would normally be reasonable in a flyer; it will go into more detail about the 12 major selling points of our software than our presentation time will allow. Having said that, however, we still want there to be "breathing room" for the design and the viewer's eyes.

We have uploaded our logo, both in full color and in white with no background (often used for watermarks, but certainly not restricted for that use alone). Our logo should be accompanied by either "Copper Vale Systems" or "Copper Vale" using the Trajan Pro font (unoriginal, we know, but it's what we've chosen). We have included a color palette that compliments our logo, but designs are not limited to that palette (for example, we have found a pink (#cc1448) that compliments the palette and that we have used in the presentation).

We have also uploaded a PSD that includes icons that could compliment 9 of the 12 major selling points for the Copper Vale Clinic Flow Platform software (the category titles are subject to change). The icons are not necessarily set in stone. For consistency with our presentation, the Protection, Integration, and Review icons should be used, but any of the remaining six (in particular, the Personalized icon) can be changed to whatever you think might be more suitable. The PSD also has some preliminary text for a few of the 12 selling points (we are refining the text now and will get the final content to designers very soon). Also note that the font is simply a placeholder; use whatever font you think would best compliment your design. Finally, keep in mind that the PSD does NOT reflect a design we are looking for; in fact, we hate this "design" and hesitate to call it a design. It was simply a way to arrange the elements to easily distribute them to designers.

We want an 8 1/2in x 11in 8-page flyer that is professional, simple, and has a clear message: this product will revolutionize your practice! We of course also need a website design that compliments the flyer design once the flyer design is finalized and chosen.

We will be monitoring this project closely-- please ask any questions you have!
Updates

Target Market(s)

Physicians, technicians, and marketing personnel in the LASIK industry.

Industry/Entity Type

Software

Number of Pages Required

4 page

Font styles to use
Serif
Sans Serif

```html
<!DOCTYPE html>
<html lang="en">
<head>
<meta charset="utf-8">
<title>Copper Vale Clinic Flow Platform – Flyer</title>
<link rel="stylesheet" href="https://fonts.googleapis.com/css2?family=Quicksand:wght@500;600;700&display=swap">
<style>
  :root {
    --teal: #20836c;
    --lime: #abc43f;
    --orange: #d2692b;
    --yellow: #f2d52c;
    --white: #ffffff;
    --navy: #1b2a38;
    --ink: #233041;
    --sky: #3aa6d9;
  }
  html, body { margin: 0; padding: 0; width: 927px; height: 1200px; overflow: hidden; background: var(--teal); }
  .canvas { width: 927px; height: 1200px; overflow: hidden; position: relative; }
  .page {
    position: absolute; left: 0; top: 0; width: 850px; height: 1100px;
    transform: scale(1.0906); transform-origin: 0 0;
    font-family: "Quicksand", sans-serif; color: var(--white);
  }
  .backdrop { position: absolute; inset: 0; }
  .brand-mark {
    position: absolute; left: 35px; top: 72px; width: 153px; height: 153px;
    box-sizing: border-box; border: 10px solid var(--white); background: var(--navy);
    display: flex; align-items: center; justify-content: center; text-align: center;
  }
  .brand-mark span { font-weight: 700; font-size: 17px; line-height: 1.25; color: var(--white); padding: 0 10px; }
  .site-url { position: absolute; right: 30px; top: 155px; font-size: 18px; font-weight: 600; color: var(--teal); }
  .headline { position: absolute; right: 42px; top: 235px; margin: 0; font-size: 18px; font-weight: 700; color: var(--yellow); letter-spacing: -0.3px; }
  .copy { position: absolute; left: 150px; width: 522px; top: 278px; text-align: right; }
  .copy p { margin: 0 0 19px; font-size: 14.3px; line-height: 19.5px; font-weight: 500; }
  .icons { position: absolute; left: 718px; top: 0; width: 70px; height: 1100px; }
  .icons svg, .icons .icon-art { position: absolute; left: 0; }
  .icon-art { background: rgba(255,255,255,0.85); border-radius: 10px; }
  .call { position: absolute; right: 46px; top: 910px; text-align: right; }
  .call .label { font-size: 22px; font-weight: 500; letter-spacing: 0.5px; }
  .call .phone { font-size: 34px; font-weight: 700; color: var(--ink); line-height: 1.05; }
  .footer-info { position: absolute; font-size: 8px; line-height: 12px; color: var(--ink); font-weight: 600; }
  .footer-info .title { color: var(--sky); }
  .address { left: 325px; top: 942px; }
  .contact { left: 325px; top: 1004px; }
  .follow { left: 468px; top: 1004px; }
</style>
</head>
<body>
<div class="canvas">
  <div class="page">
    <svg class="backdrop" viewBox="0 0 850 1100" width="850" height="1100" aria-hidden="true">
      <rect width="850" height="1100" fill="var(--teal)"/>
      <polygon points="0,0 150,0 0,40" fill="var(--lime)"/>
      <polygon points="150,0 850,0 850,10 140,10" fill="var(--orange)"/>
      <polygon points="0,148 445,148 372,175 0,175" fill="var(--lime)"/>
      <polygon points="455,158 850,22 850,235 590,235" fill="var(--yellow)"/>
      <polygon points="0,318 850,8 850,28 0,334" fill="var(--white)"/>
      <polygon points="0,770 600,905 850,862 850,1100 0,1100" fill="var(--orange)"/>
      <polygon points="540,935 850,862 850,1100 400,1100" fill="var(--lime)"/>
      <polygon points="0,1030 250,1100 0,1100" fill="var(--lime)"/>
    </svg>

    <div class="brand-mark"><span>Copper Vale Systems</span></div>
    <div class="site-url">www.yoursitenamehere.com</div>
    <h1 class="headline">We Can Help You With 15 Experience!</h1>

    <div class="copy">
      <p>It's time for a revolution in an industry that depends on effective marketing, tracking marketing campaign effectiveness, and converting interest into procedures. Finally comes the solution: the Copper Vale Clinic Flow Platform which includes connectivity between your marketing records and your patient records. Two databases, one for patients and one for prospective patients, with a single program connecting them. It's simple, it's HIPAA-compliant, and it's only the beginning.</p>
      <p>Contact with prospective and current patients is key in a market of elective procedures. Communication must be efficient, standardized, but also personalized. The Copper Vale Clinic Flow Platform does it all by incorporating the patient and contact database information in your communications. The Suite offers an array of customizable, personalized emails, texts, and even printouts for appointment reminders, surgery prepartion information, and referral programs - all with a few clicks.</p>
      <p>In the digital age our industry still requires patients to fill out forms with pen and paper which in turn have to be entered into a database by hand. Technicians must take digital information from [device], print it out into physical paper, then enter the data back into digital format. We say, "No more." With the Copper Vale Clinic Flow Platform your practice will enjoy full digital integration of all key equipment, including the laser, the Wavefront, and the HIPAA-compliant databases that connect them.</p>
      <p>With your key devices linked together in an integrated system, the Copper Vale Clinic Flow Platform offers significant protection for you and your practice. In addition to streamlining operations, not having to enter data multiple times means you are protected from human errors that can lead to lawsuits.</p>
    </div>

    <div class="icons">
      <svg style="top:276px" width="66" height="50" viewBox="0 0 66 50" aria-label="Exchange arrows" role="img">
        <polygon points="2,6 26,6 26,0 40,12 26,24 26,18 2,18" fill="var(--white)"/>
        <polygon points="64,30 40,30 40,24 26,36 40,48 40,42 64,42" fill="var(--white)"/>
      </svg>
      <div class="icon-art" style="top:370px;left:6px;width:50px;height:64px;border-radius:50% 50% 40% 40%" role="img" aria-label="Fingerprint icon"></div>
      <div class="icon-art" style="top:483px;left:2px;width:58px;height:58px" role="img" aria-label="Puzzle pieces icon"></div>
      <svg style="top:577px" width="62" height="60" viewBox="0 0 62 60" aria-label="Umbrella" role="img">
        <path d="M4,26 Q31,-4 58,26 Z" fill="var(--white)"/>
        <path d="M31,26 V50 Q31,57 25,57 Q20,57 20,52" stroke="var(--white)" stroke-width="3" fill="none"/>
      </svg>
      <svg style="top:658px" width="62" height="72" viewBox="0 0 62 72" aria-label="Compass" role="img">
        <rect x="26" y="0" width="10" height="8" rx="2" fill="var(--white)"/>
        <circle cx="31" cy="40" r="27" fill="var(--white)"/>
        <circle cx="31" cy="40" r="21" fill="var(--teal)"/>
        <polygon points="31,22 36,40 31,58 26,40" fill="var(--white)"/>
      </svg>
      <svg style="top:764px" width="62" height="66" viewBox="0 0 62 66" aria-label="Growth chart" role="img">
        <rect x="4" y="52" width="7" height="12" fill="var(--white)"/>
        <rect x="14" y="46" width="7" height="18" fill="var(--white)"/>
        <rect x="24" y="40" width="7" height="24" fill="var(--white)"/>
        <rect x="34" y="32" width="7" height="32" fill="var(--white)"/>
        <rect x="44" y="24" width="7" height="40" fill="var(--white)"/>
        <path d="M2,44 Q36,36 50,10" stroke="var(--white)" stroke-width="4" fill="none"/>
        <polygon points="42,8 58,0 56,18" fill="var(--white)"/>
      </svg>
    </div>

    <div class="call">
      <div class="label">CALL US NOW!</div>
      <div class="phone">1-888-555-0142</div>
    </div>

    <div class="footer-info address">
      <div class="title">YOUR ADDRESS HERE</div>
      <div>Street 1 text goes here</div>
      <div>Street 2 text goes here</div>
      <div>postcode, state, country</div>
    </div>
    <div class="footer-info contact">
      <div class="title">CONTACT US</div>
      <div>P: 012 3456 7890</div>
      <div>F: 012 3456 7890</div>
      <div>E: mail@coppervale.example</div>
    </div>
    <div class="footer-info follow">
      <div class="title">FOLLOW US @</div>
      <div>social.example/coppervale</div>
      <div>updates.example/coppervale</div>
      <div>network.example/coppervale</div>
    </div>
  </div>
</div>
</body>
</html>
```